Major Australian Food and Wine Event Web Design Project

The project will consist of 3 designs
The homepage
A city hub page
A general content page

The main audience who will visit the website will be (in Order of importance:

1) Visitors
- Mainly women 24 – 54 years (they are the main ticket buyers)
- In a relationship – so will go to the show with their partner
- In a good paying job or home maker – and who have disposable income to spend $30 a ticker
- Enjoy food, wine and going out
- Looking for a fun day out – although an event that is about food and wine – it is an event that most people will go to and have a fun day out – not too pretentious

A smaller proportion of the audience will be:
2) Exhibitors & sponsors ( both prospective and existing)
3) Media

Objectives:

- Functionality on home page and sub pages needs to be updated, clear, easy to navigate and inject a sense of ‘fun’ – need to make it look more professional
- Need to incorporate the many things that need to be on the home page and sub pages in a visually appealing manner
- Ensure the ‘Cons’ above are considered and reflected in functionality and design
- To not be too focus on the colours (these can be changed) – but focus on the functionality and overall design opportunities.

Approach:

Keywords to describe the Bright Plate & Vine Fair:
Fun day out, discover, learn, indulge, entertaining

Other website examples:

Some great consumers event websites from the UK really make our website look basic and juvenile – and below are some examples of the presentation of how we would like our website to look like:

http://www.morselfairs-example.com/london/ This website is clean, includes good social media integration and exudes a sense of fun. Their content pages, such as the features landing page also presents options in a clear and visually appealing way with a series of boxes including image and text http://www.morselfairs-example.com/london/content/343/Features

http://www.homecraftexpo-example.com/ - this is also a great website – and it incorporates all the elements we would be looking for on our homepage – but the background/skin also includes a sense of fun and cheekiness. Subpages also are consistent.

Features

• Its a fun day that offers great value for money
• Caters to all visitors, regardless of different levels of knowledge or interest in food, wine and cooking.
• Sample great quality food and wine products from hundreds of reputable exhibitors
• Learn more through many of the shows feature activities (Celeb Theatre, Wine Theatre, Cooking & Cheese Classes)

Functionality & Structure:

In a user friendly, easy to view way, we need to incorporate the following functionality elements on home page:
- main header (that will incorporate our current creative) with a ‘fun’ skin
- navigation tabs/references (hone, location, tickets, blog, sign up, exhibitors)
- navigation/content banner (rotating)
- Area for small intro about the show
- News and highlight section
- New exhibitors section
- Obvious Ticket call to action
- Obvious sign up call to action
- Social media buttons or links ( really like the moving gifs on the Homecraftexpo-example.com site
- area for advertising (MREC size) to sell to exhibitors/sponsors
- Show dates for all 5 shows (maybe in main header)

Subpage layout is also important and needs to reflect the homepage – so would also like to see examples of how this would look and tie in with navigation – we generally have a lot of content on these pages, so clear navigation would be useful. – see below for further details of functionality for city Hubs

‘CITY HUB’ BRIEF
When navigating to each location the user will be taken to a ‘CITY HUB’ which should replicate design and content elements of a main HOME page, as well as reflect more specific information for each Show. Elements which must appear on this page are:
• FEATURES – which may be displayed in categories (in boxes, see appendix 1.0) which will link through to relevant content pages. Or in one box which will link through to a features page with all presented in boxes
• CHEFS – may be displayed as a separate icon box which will link to chefs page with bios, Celeb Theatre timetable etc.
• TICKETS – either a button or clear callout to purchase tickets
• PLAN YOUR DAY – may be displayed in a separate content box which will then link through to getting there, sample itineraries and downloadable pocket show guide for visitors to print before coming to the Show.
• WHO’S EXHIBITING – to link back to city specific exhibitor lists

Our current website is out of date and has the following inadequacies (www.brightplatefair-example.com.au) -

The homepage
A city hub page
A general content page

1) Visitors

3) Media

Objectives:

Approach:

To be perceived as a fun, entertaining event with something for everyone - website creative and navigation must reflect this.

Other website examples:

Features

- New exhibitors section

‘CITY HUB’ BRIEF

- Dated design/layout
- Homepage too text heavy
- No content boxes that can be used for different features/areas (eg. News, Exhibitors etc)
- Uninspiring colours and skin(eg. grey background), does not reflect ‘a fun day out’
- Limited presence of social media platforms and lacks ‘community’
- No continuity in sub pages
- main banner too big – takes up too much space on homepage

Requirements
Must have
• As per above brief.

In addition:
Floating social media buttons on side
Wrap around image
Drop down menu (specifically for the location nav item)

```html
<!DOCTYPE html>
<html lang="en">
<head>
<meta charset="utf-8">
<title>Bright Plate &amp; Vine Fair</title>
<link href="https://fonts.googleapis.com/css2?family=Arimo:wght@400;700&family=PT+Serif:ital,wght@1,700&display=swap" rel="stylesheet">
<style>
:root{
  --red:#c4161c;
  --red-dark:#8e0f13;
  --orange:#f28c1e;
  --cream:#f4efe2;
  --vine-top:#dfe3cf;
  --vine-mid:#b7b98f;
  --wood:#3b2414;
  --wood-dark:#24150b;
  --text:#444;
  --muted:#777;
  --line:#e2e2e2;
  --white:#fff;
}
*{margin:0;padding:0;box-sizing:border-box}
html,body{width:829px;height:1200px;overflow:hidden}
body{position:relative;font-family:"Arimo",Arial,sans-serif;color:var(--text);font-size:9px;line-height:1.4;
  background:linear-gradient(180deg,var(--vine-top) 0,#cdd1b3 300px,var(--vine-mid) 600px,#8d8a63 900px,var(--wood) 925px)}
.abs{position:absolute}

/* header */
.brand{left:18px;top:14px;width:250px;display:flex;align-items:center;gap:8px}
.brand-mark{width:34px;height:34px;border-radius:50%;background:var(--red);flex:none}
.brand-name{font-weight:700;font-size:17px;color:var(--red);line-height:1.1}
.tagline{left:300px;top:16px;font-family:"PT Serif",serif;font-style:italic;font-weight:700;font-size:18px;color:var(--red-dark)}
.call{left:650px;top:14px;width:165px;height:24px;background:var(--red);color:var(--white);border-radius:12px;font-weight:700;font-size:11px;text-align:center;line-height:24px}
.nav{left:293px;top:52px;width:530px;height:22px;background:var(--red-dark);display:flex;border-radius:3px}
.nav a{flex:1;color:var(--white);text-decoration:none;font-size:8px;font-weight:700;text-align:center;line-height:22px;border-right:1px solid rgba(255,255,255,.25)}
.nav a.active{background:var(--red)}
.plates{left:300px;top:82px;width:515px;height:68px;border-radius:6px;
  background:radial-gradient(circle at 10% 60%,#e8542a 0 22px,transparent 24px),radial-gradient(circle at 35% 55%,#f3a23a 0 24px,transparent 26px),radial-gradient(circle at 62% 60%,#d93a2a 0 22px,transparent 24px),radial-gradient(circle at 88% 55%,#f07a2a 0 24px,transparent 26px),linear-gradient(90deg,#efe8d6,#f7f2e6)}
.hook{left:62px;top:114px;font-size:12px;color:var(--red);font-weight:700}
.hook span{display:block;font-size:9px;color:#333;font-weight:400}

/* main panel */
.panel{left:60px;top:150px;width:735px;height:772px;background:var(--white);box-shadow:0 0 6px rgba(0,0,0,.25)}
.slider{left:68px;top:156px;width:719px;height:146px;background:linear-gradient(110deg,#55504a,#8b8277 45%,#c9c1b2 75%,#e3ddd0)}
.promo{left:548px;top:166px;width:232px;height:68px;background:var(--red);color:var(--white);padding:8px 10px}
.promo h3{font-size:11px;line-height:1.2;text-transform:uppercase}
.promo p{font-size:8px;margin-top:3px}
.promo .btn{position:absolute;left:10px;top:74px;background:var(--red-dark);padding:3px 10px;font-size:8px;font-weight:700;color:var(--white)}
.ribbon{left:68px;top:282px;width:200px;height:20px;background:var(--red);color:var(--white);font-weight:700;font-size:10px;text-transform:uppercase;line-height:20px;padding-left:12px}
.dots{left:640px;top:290px;display:flex;gap:4px}
.dots i{width:7px;height:7px;border-radius:50%;background:var(--white);opacity:.6}
.dots i:first-child{opacity:1;background:var(--red)}

.intro{left:76px;top:312px;width:462px}
.intro h2{color:var(--red);font-size:12px;margin-bottom:6px}
.intro p{margin-bottom:6px;color:var(--text)}
.intro ul{list-style:none;margin-bottom:6px}
.intro li{padding-left:10px;position:relative}
.intro li::before{content:"";position:absolute;left:0;top:4px;width:5px;height:5px;background:var(--red)}
.signup-label{left:76px;top:486px;font-weight:700;font-size:9px;color:#333}
.signup-input{left:76px;top:500px;width:280px;height:18px;border:1px solid #ccc;background:var(--white)}
.signup-btn{left:362px;top:500px;width:60px;height:18px;background:var(--red);color:var(--white);font-weight:700;font-size:8px;text-align:center;line-height:18px}

.blog{left:552px;top:312px;width:235px;height:236px;border:1px solid var(--line);padding:8px}
.blog h3{color:var(--red);font-size:12px;border-bottom:1px solid var(--line);padding-bottom:4px;margin-bottom:6px}
.blog .post{margin-bottom:7px}
.blog .post b{display:block;font-size:8px;color:#333}
.blog .post p{font-size:8px;color:var(--muted)}
.blog .btn{position:absolute;right:8px;bottom:8px;background:var(--red);color:var(--white);font-size:8px;font-weight:700;padding:3px 10px}

.cities{left:76px;top:566px;width:704px;display:flex;gap:8px}
.city{flex:1}
.city .photo{height:62px;border-radius:2px}
.city span{display:block;text-align:center;font-weight:700;font-size:10px;color:#222;margin-top:5px;text-transform:uppercase}

.box{top:700px;width:226px;height:214px;border:1px solid var(--line)}
.tabs{display:flex;height:18px}
.tabs b{background:var(--red);color:var(--white);font-size:8px;padding:0 10px;line-height:18px}
.tabs b+b{background:#ddd;color:#555}
.item{display:flex;gap:6px;padding:6px 6px 0}
.thumb{width:52px;height:40px;flex:none;border-radius:2px}
.item p{font-size:7.5px;color:var(--muted)}
.item p b{display:block;color:var(--red);font-size:8px}
.box .btn{position:absolute;right:6px;bottom:6px;background:var(--red);color:var(--white);font-size:8px;font-weight:700;padding:3px 8px}
.fantasy{left:548px;top:700px;width:239px;height:104px;background:linear-gradient(135deg,#6b3b22,#b5653a 60%,#d9a36a)}
.fantasy span{position:absolute;left:10px;bottom:10px;color:var(--white);font-weight:700;font-size:11px;text-transform:uppercase;width:150px;line-height:1.2}
.advert{left:548px;top:812px;width:239px;height:102px;background:#ececec;border:1px solid #ddd;color:#999;font-size:11px;display:flex;align-items:center;justify-content:center}

.tickets-tab{left:50px;top:370px;width:20px;height:110px;background:var(--orange);border-radius:3px 0 0 3px}
.tickets-tab span{position:absolute;left:3px;top:100px;transform:rotate(-90deg);transform-origin:left top;color:var(--white);font-weight:700;font-size:9px;white-space:nowrap}
.social{left:798px;top:388px;display:flex;flex-direction:column;gap:4px}
.social i{width:16px;height:16px;border-radius:2px}

.footer{left:0;top:925px;width:829px;height:245px;background:linear-gradient(180deg,var(--wood),var(--wood-dark))}
.fcol{top:945px;color:#d9cbb5;font-size:8px}
.fcol h4{color:var(--white);font-size:9px;text-transform:uppercase;margin-bottom:6px}
.fcol li{list-style:none;line-height:1.7}
.news{left:560px;top:940px;width:235px}
.news h4{color:var(--white);font-size:12px;margin-bottom:5px}
.news p{color:#d9cbb5;font-size:8px;margin-bottom:6px}
.news .field{height:16px;background:var(--white);margin-bottom:5px}
.news .go{display:inline-block;background:var(--red);color:var(--white);font-weight:700;font-size:8px;padding:3px 10px}
.copy{left:0;top:1170px;width:829px;height:30px;background:#160c05;color:#9c8b74;font-size:8px;line-height:30px;padding:0 60px;display:flex;justify-content:space-between}
</style>
</head>
<body>

<div class="abs brand"><div class="brand-mark"></div><div class="brand-name">Bright Plate &amp; Vine Fair</div></div>
<div class="abs tagline">Major Australian Food and Wine Event</div>
<div class="abs call">Call Now: 1300 555 019</div>
<nav class="abs nav"><a class="active">HOME</a><a>LOCATIONS</a><a>TICKETS</a><a>BLOG</a><a>SIGN UP</a><a>EXHIBITORS</a><a>CONTACT US</a></nav>
<div class="abs plates" role="img" aria-label="Row of plated dishes and fresh tomatoes"></div>
<div class="abs hook">Looking for a fun day out<span>An event that is about food and wine</span></div>

<div class="abs panel"></div>
<div class="abs slider" role="img" aria-label="Chefs presenting dishes beside glasses of wine"></div>
<div class="abs promo"><h3>Indulge your passion for regional premium wines</h3><p>Visit the Vine Wine Theatre 2013</p><span class="btn">Click more</span></div>
<div class="abs ribbon">Welcome to your senses</div>
<div class="abs dots"><i></i><i></i><i></i><i></i></div>

<section class="abs intro">
  <h2>The Bright Plate &amp; Vine Fair - All over for another year!</h2>
  <p>Melbourne, Sydney, Perth, Adelaide and Brisbane have all had the chance to experience the fun, excitement and joy that is the Bright Plate &amp; Vine Fair. We would like to thank all our amazing visitors for coming along and helping us celebrate another fabulous year. We hope you had a great day out with the many exciting exhibitors, sponsors and chefs.</p>
  <ul>
    <li>It's a fun day that offers great value for money</li>
    <li>Caters to all visitors, regardless of different levels of knowledge or interest in food, wine and cooking</li>
    <li>Sample great quality food and wine products from hundreds of reputable exhibitors</li>
    <li>Learn more through many of the fair's feature activities (Celeb Theatre, Wine Theatre, Cooking &amp; Cheese Classes)</li>
  </ul>
  <p>Make sure you visit the website early next year for all the details of the 2013 shows, or sign up to our newsletter to be the first to find out when we are on sale and to receive special offers.</p>
</section>
<div class="abs signup-label">Sign up to the Bright Plate &amp; Vine Fair e-newsletter</div>
<div class="abs signup-input"></div>
<div class="abs signup-btn">Submit</div>

<aside class="abs blog">
  <h3>Latest Blog</h3>
  <div class="post"><b>Bright Plate &amp; Vine Fair</b><p>Fresh recipes, tasting notes and kitchen tips from our chefs, plus news on classes and theatre sessions coming up at the next fair.</p></div>
  <div class="post"><b>Bright Plate &amp; Vine Fair</b><p>Meet the new exhibitors joining us this season and see which regional wines are set to pour at the tasting bars.</p></div>
  <div class="post"><b>Bright Plate &amp; Vine Fair</b><p>Plan your day with our handy guide to the best stalls.</p></div>
  <span class="btn">Click here for more</span>
</aside>

<div class="abs cities">
  <div class="city"><div class="photo" role="img" aria-label="Melbourne skyline" style="background:linear-gradient(#7fa6c9,#3d5d7a)"></div><span>Melbourne</span></div>
  <div class="city"><div class="photo" role="img" aria-label="Sydney harbour" style="background:linear-gradient(#8bb8d8,#2f5f86)"></div><span>Sydney</span></div>
  <div class="city"><div class="photo" role="img" aria-label="Perth city at dusk" style="background:linear-gradient(#e0a06a,#4c3a5a)"></div><span>Perth</span></div>
  <div class="city"><div class="photo" role="img" aria-label="Crowd at the Adelaide fair" style="background:linear-gradient(#c9a27a,#6a4a34)"></div><span>Adelaide</span></div>
  <div class="city"><div class="photo" role="img" aria-label="Brisbane river view" style="background:linear-gradient(#9cc3d6,#3e6a58)"></div><span>Brisbane</span></div>
</div>

<div class="abs box" style="left:76px">
  <div class="tabs"><b>HIGHLIGHTS</b><b>FEATURES</b></div>
  <div class="item"><div class="thumb" role="img" aria-label="Cooking class dish" style="background:#c9673a"></div><p>Lorem ipsum is simply dummy text of the printing and type setting industry.<b>Read more</b></p></div>
  <div class="item"><div class="thumb" role="img" aria-label="Wine tasting glasses" style="background:#8a2a2a"></div><p>Lorem ipsum is simply dummy text of the printing and type setting industry.<b>Read more</b></p></div>
  <div class="item"><div class="thumb" role="img" aria-label="Cheese platter" style="background:#e0b556"></div><p>Lorem ipsum is simply dummy text of the printing and type setting industry.<b>Read more</b></p></div>
  <span class="btn">View all highlights</span>
</div>
<div class="abs box" style="left:312px">
  <div class="tabs"><b>CHEFS</b><b>WINERIES</b></div>
  <div class="item"><div class="thumb" role="img" aria-label="Chef at a cooking station" style="background:#b7a48a"></div><p>Lorem ipsum is simply dummy text of the printing and type setting industry.<b>Read more</b></p></div>
  <div class="item"><div class="thumb" role="img" aria-label="Chef plating a dish" style="background:#9a8570"></div><p>Lorem ipsum is simply dummy text of the printing and type setting industry.<b>Read more</b></p></div>
  <div class="item"><div class="thumb" role="img" aria-label="Chef in the theatre kitchen" style="background:#a99278"></div><p>Lorem ipsum is simply dummy text of the printing and type setting industry.<b>Read more</b></p></div>
  <span class="btn">View all Chefs</span>
</div>
<div class="abs fantasy" role="img" aria-label="Gourmet dish close-up"><span>Indulge all your foodie fantasies</span></div>
<div class="abs advert">Area for Advertising</div>

<div class="abs tickets-tab"><span>BUY TICKETS</span></div>
<div class="abs social"><i style="background:#3b5998"></i><i style="background:#2ba6de"></i><i style="background:#c4302b"></i><i style="background:#0e76a8"></i><i style="background:#e37b1f"></i></div>

<footer class="abs footer"></footer>
<div class="abs fcol" style="left:60px"><h4>Bright Plate Locations</h4><ul><li>Melbourne</li><li>Sydney</li><li>Perth</li><li>Adelaide</li><li>Brisbane</li></ul></div>
<div class="abs fcol" style="left:200px"><h4>Show and Attractions</h4><ul><li>Tickets</li><li>Exhibitors</li><li>Chefs</li><li>Wine Theatre</li><li>Cooking Classes</li></ul></div>
<div class="abs fcol" style="left:340px"><h4>Bright Plate Chef Rec's</h4><ul><li>Ana Ruiz</li><li>Tom Hale</li><li>Mia Storr</li><li>Leo Brandt</li><li>Kit Moran</li></ul></div>
<div class="abs news"><h4>Newsletter Signup</h4><p>Sign up to our newsletter and receive early updates on the next fair and special offers.</p><div class="field"></div><div class="field"></div><span class="go">SIGN ME UP</span></div>
<div class="abs copy"><span>© Copyright 2013 Bright Plate &amp; Vine Fair. All rights reserved.</span><span>Website Design &amp; Development</span></div>

</body>
</html>
```